Electronic hardware design and manufacturer needing a new business card design.

We need a new business card design consisting of a double sided design adhering to brand and logo guidelines attached. I also want to incorporate something that recognizes our 25th year in business ("EST 2001" or something like that....).

Need extra days to review

Need extra days to review

```html
<!DOCTYPE html>
<html lang="en">
<head>
<meta charset="utf-8">
<title>Kestrel Circuit Corp. – Business Card</title>
<link href="https://fonts.googleapis.com/css2?family=Montserrat:wght@300;400;600;700&family=Inter:wght@400;500&display=swap" rel="stylesheet">
<style>
  :root {
    --page: #e0e0e0;
    --navy: #082639;
    --steel: #9bb5d4;
    --white: #ffffff;
    --orange: #e07a2c;
    --grey-text: #444a50;
    --grey-soft: #7c7c7c;
    --rule: #9a9a9a;
    --band-1: #8b1f23;
    --band-2: #d9502c;
    --band-3: #f47c30;
    --band-4: #fbb732;
  }
  * { margin: 0; padding: 0; box-sizing: border-box; }
  html, body { width: 1200px; height: 1200px; overflow: hidden; }
  body { background: var(--page); position: relative; font-family: "Montserrat", sans-serif; }

  .card { position: absolute; left: 179px; width: 861px; height: 496px; overflow: hidden; }
  .card--front { top: 84px; background: var(--navy); }
  .card--back { top: 622px; background: var(--white); }

  /* Front */
  .front__est {
    position: absolute; left: 27px; top: 172px;
    font-family: "Montserrat", sans-serif; font-weight: 600; font-size: 41px; letter-spacing: 2px;
    color: var(--steel);
  }
  .front__brand {
    position: absolute; right: 60px; bottom: 38px; width: 300px; text-align: right;
    font-family: "Montserrat", sans-serif; font-weight: 700; font-size: 40px; line-height: 1.05;
    color: var(--steel); text-transform: uppercase;
  }

  /* Back */
  .back__mark { position: absolute; left: 82px; top: 150px; width: 300px; }
  .back__est {
    font-weight: 700; font-size: 26px; letter-spacing: 1.5px; color: var(--navy);
    margin-left: 12px;
  }
  .back__brand-row { display: flex; align-items: center; gap: 12px; margin-top: 8px; }
  .back__square { width: 22px; height: 22px; background: var(--band-3); flex: none; }
  .back__brand {
    font-weight: 700; font-size: 34px; line-height: 1.05; color: var(--navy); text-transform: uppercase;
  }

  .back__divider {
    position: absolute; left: 431px; top: 120px; width: 2px; height: 256px; background: var(--rule);
  }
  .back__divider::before {
    content: ""; position: absolute; left: 0; top: 0; width: 2px; height: 56px; background: var(--orange);
  }

  .person { position: absolute; left: 451px; top: 108px; }
  .person__name { font-weight: 600; font-size: 39px; letter-spacing: 0.5px; color: var(--orange); line-height: 1.15; }
  .person__role { font-weight: 300; font-size: 28px; color: var(--grey-soft); line-height: 1.05; letter-spacing: 1px; }

  .address {
    position: absolute; left: 454px; top: 193px;
    font-family: "Inter", sans-serif; font-weight: 500; font-size: 22px; letter-spacing: 1.5px;
    line-height: 34px; color: var(--grey-text); font-style: normal;
  }

  .contact { position: absolute; left: 450px; top: 270px; list-style: none; }
  .contact__item {
    display: flex; align-items: center; height: 38px;
    font-family: "Inter", sans-serif; font-weight: 500; font-size: 22px; letter-spacing: 1.5px; color: var(--grey-text);
  }
  .contact__icon { width: 26px; height: 26px; margin-right: 18px; flex: none; }

  .band { position: absolute; left: 0; bottom: 0; width: 100%; height: 18px; display: flex; }
  .band span { flex: 1; }
  .band .b1 { background: var(--band-1); }
  .band .b2 { background: var(--band-2); }
  .band .b3 { background: var(--band-3); }
  .band .b4 { background: var(--band-4); }
</style>
</head>
<body>

<section class="card card--front">
  <div class="front__est">EST 2001</div>
  <div class="front__brand">Kestrel Circuit Corp.</div>
</section>

<section class="card card--back">
  <div class="back__mark">
    <div class="back__est">EST 2001</div>
    <div class="back__brand-row">
      <span class="back__square"></span>
      <span class="back__brand">Kestrel Circuit Corp.</span>
    </div>
  </div>

  <div class="back__divider"></div>

  <div class="person">
    <div class="person__name">NORA KELLAND</div>
    <div class="person__role">President</div>
  </div>

  <address class="address">
    4410 Ridge Road NE, Unit 12<br>
    Red Deer, Alberta T4N 5E2
  </address>

  <ul class="contact">
    <li class="contact__item">
      <svg class="contact__icon" viewBox="0 0 26 26" fill="none" stroke="#e07a2c" stroke-width="2" stroke-linecap="round" stroke-linejoin="round">
        <path d="M6 3l4 1 1 5-3 2a13 13 0 0 0 7 7l2-3 5 1 1 4c0 1-1 3-3 3A20 20 0 0 1 3 6c0-2 2-3 3-3z"/>
        <path d="M15 4a8 8 0 0 1 7 7"/>
        <path d="M15 8a4 4 0 0 1 3 3"/>
      </svg>
      (403) 555-0148
    </li>
    <li class="contact__item">
      <svg class="contact__icon" viewBox="0 0 26 26" fill="none" stroke="#e07a2c" stroke-width="2" stroke-linejoin="round">
        <rect x="2" y="6" width="22" height="15"/>
        <path d="M2 6l11 9 11-9M2 21l8-7M24 21l-8-7"/>
      </svg>
      hello@kestrelcc.ca
    </li>
    <li class="contact__item">
      <svg class="contact__icon" viewBox="0 0 26 26" fill="none" stroke="#e07a2c" stroke-width="2">
        <circle cx="13" cy="13" r="11"/>
        <ellipse cx="13" cy="13" rx="5" ry="11"/>
        <path d="M2 13h22M4 7h18M4 19h18"/>
      </svg>
      kestrelcc.ca
    </li>
  </ul>

  <div class="band"><span class="b1"></span><span class="b2"></span><span class="b3"></span><span class="b4"></span></div>
</section>

</body>
</html>
```